Bref créative
Stationary for Ministry
R L Brandt Harvest Ministries
Use same font as used in my logo
Can modify at designer's discretion
Professional
R L Brandt
Founder
418 W. Corvell Blvd
Longview, TX 75612
rlbtx7@mailvane.net
rlbrandt.com
just put the logo on the front
all contact info on back
Hello! This file should be in a transparent format so no lines or shadows show up.

```html
<!DOCTYPE html>
<html lang="en">
<head>
<meta charset="utf-8">
<title>R L Brandt Harvest Ministries — Stationery</title>
<link rel="stylesheet" href="https://fonts.googleapis.com/css2?family=Quicksand:wght@700&family=Open+Sans:wght@400;600&display=swap">
<style>
  :root {
    --paper: #ffffff;
    --backdrop: #ffffff;
    --blue: #1b8fd8;
    --blue-deep: #0c6bb3;
    --blue-light: #6cc0f0;
    --leaf-green: #9ccb5a;
    --leaf-orange: #f2b56b;
    --ink: #555a60;
    --edge: #e3e6ea;
  }
  html, body {
    margin: 0;
    padding: 0;
    width: 1200px;
    height: 634px;
    overflow: hidden;
    background: var(--backdrop);
  }
  .stationery { display: block; width: 1200px; height: 634px; }
  .brand-name { font-family: "Quicksand", sans-serif; font-weight: 700; fill: var(--blue); }
  .brand-mark { fill: var(--leaf-green); }
  .faint .brand-name, .faint .brand-mark { opacity: 0.14; }
  .contact { font-family: "Open Sans", sans-serif; font-size: 5px; fill: var(--ink); }
  .contact-strong { font-family: "Open Sans", sans-serif; font-size: 6px; font-weight: 600; fill: var(--ink); }
  .card-white { fill: var(--paper); stroke: var(--edge); stroke-width: 1; }
  .caption { font-family: "Open Sans", sans-serif; font-size: 12px; letter-spacing: 0.5px; fill: #333; }
  .blue { fill: var(--blue); }
  .blue-deep { fill: var(--blue-deep); }
</style>
</head>
<body>
<svg class="stationery" viewBox="0 0 1200 634" xmlns="http://www.w3.org/2000/svg">
  <defs>
    <linearGradient id="band" x1="0" y1="0" x2="1" y2="0">
      <stop offset="0" stop-color="#6cc0f0"/>
      <stop offset="1" stop-color="#0c6bb3"/>
    </linearGradient>
    <linearGradient id="cardBlue" x1="0" y1="0" x2="1" y2="1">
      <stop offset="0" stop-color="#3aa6e8"/>
      <stop offset="1" stop-color="#0c6bb3"/>
    </linearGradient>
    <radialGradient id="discShine" cx="0.5" cy="0.5" r="0.5">
      <stop offset="0.2" stop-color="#ffffff"/>
      <stop offset="1" stop-color="#e4e8ee"/>
    </radialGradient>
  </defs>

  <!-- Business card front: name and contact -->
  <g class="business-card card-front">
    <rect class="card-white" x="34" y="43" width="153" height="96" rx="3"/>
    <text class="contact-strong" x="42" y="54">R L Brandt - Founder</text>
    <g class="brand-lockup">
      <circle class="brand-mark" cx="46" cy="80" r="5"/>
      <text class="brand-name" x="54" y="84" font-size="11">RL BRANDT</text>
      <text class="brand-name" x="54" y="91" font-size="4.2">HARVEST MINISTRIES</text>
    </g>
    <text class="contact" x="42" y="110">418 W. Corvell Blvd</text>
    <text class="contact" x="42" y="117">Longview, TX 75612</text>
    <text class="contact" x="42" y="126">rlbrandt.com</text>
    <text class="contact" x="112" y="110">(903) 555-0148</text>
    <text class="contact" x="112" y="117">(903) 555-0172</text>
    <text class="contact" x="112" y="126">rlbtx7@mailvane.net</text>
  </g>

  <!-- Business card: white with blue sweep -->
  <g class="business-card card-sweep">
    <rect class="card-white" x="34" y="221" width="153" height="96" rx="3"/>
    <path fill="url(#band)" d="M120 317 C150 300 175 270 187 221 L187 317 Z"/>
    <g class="brand-lockup">
      <circle class="brand-mark" cx="50" cy="262" r="6"/>
      <text class="brand-name" x="60" y="267" font-size="14">RL BRANDT</text>
      <text class="brand-name" x="60" y="276" font-size="5.4">HARVEST MINISTRIES</text>
    </g>
  </g>

  <!-- Business card: blue back -->
  <g class="business-card card-back">
    <rect x="34" y="377" width="153" height="96" rx="3" fill="url(#cardBlue)"/>
    <rect x="40" y="372" width="153" height="96" rx="3" fill="url(#cardBlue)" opacity="0.5"/>
    <rect x="34" y="377" width="153" height="96" rx="3" fill="url(#cardBlue)"/>
    <circle cx="48" cy="418" r="6" fill="var(--paper)"/>
    <text class="brand-name" x="58" y="423" font-size="14" fill="#ffffff" style="fill:#ffffff">RL BRANDT</text>
    <text class="brand-name" x="58" y="432" font-size="5.4" style="fill:#ffffff">HARVEST MINISTRIES</text>
  </g>

  <!-- Envelope -->
  <g class="envelope">
    <rect class="card-white" x="252" y="43" width="528" height="269"/>
    <path fill="url(#band)" d="M252 43 H780 V312 C770 230 720 130 560 108 C430 92 330 110 252 120 Z" opacity="0"/>
    <path fill="url(#band)" d="M252 43 H730 L780 68 V108 C640 92 420 92 252 108 Z"/>
    <path class="blue" d="M740 120 C765 160 778 230 780 312 L780 110 Z"/>
    <g class="brand-lockup">
      <circle class="brand-mark" cx="296" cy="134" r="7"/>
      <text class="brand-name" x="307" y="140" font-size="16">RL BRANDT</text>
      <text class="brand-name" x="307" y="149" font-size="6">HARVEST MINISTRIES</text>
    </g>
    <text class="contact" x="290" y="232">418 W. Corvell Blvd</text>
    <text class="contact" x="290" y="239">Longview, TX 75612</text>
    <text class="contact" x="290" y="246">rlbrandt.com</text>
    <text class="contact" x="352" y="232">(903) 555-0148</text>
    <text class="contact" x="352" y="239">(903) 555-0172</text>
    <text class="contact" x="352" y="246">rlbtx7@mailvane.net</text>
    <rect role="img" aria-label="Light tree illustration with green and orange leaves" x="660" y="180" width="100" height="120" rx="40" fill="var(--leaf-green)" opacity="0.22"/>
  </g>

  <!-- CD sleeve -->
  <g class="cd-sleeve">
    <rect class="card-white" x="307" y="331" width="176" height="222"/>
    <path class="blue" d="M466 331 H483 V553 H466 C476 480 476 400 466 331 Z"/>
    <g class="brand-lockup">
      <circle class="brand-mark" cx="322" cy="356" r="5"/>
      <text class="brand-name" x="330" y="360" font-size="11">RL BRANDT</text>
      <text class="brand-name" x="330" y="367" font-size="4.2">HARVEST MINISTRIES</text>
    </g>
    <rect role="img" aria-label="Faint large tree illustration in green and orange" x="330" y="385" width="120" height="140" rx="55" fill="var(--leaf-orange)" opacity="0.2"/>
    <text class="contact" x="360" y="543">rlbrandt.com · rlbtx7@mailvane.net</text>
  </g>

  <!-- CD disc -->
  <g class="cd-disc">
    <circle cx="595" cy="444" r="96" fill="url(#discShine)" stroke="var(--edge)"/>
    <circle cx="595" cy="444" r="30" fill="#f4f6f8" stroke="var(--edge)"/>
    <circle cx="595" cy="444" r="11" fill="var(--backdrop)" stroke="#c9ced5"/>
    <g class="brand-lockup">
      <circle class="brand-mark" cx="536" cy="398" r="5"/>
      <text class="brand-name" x="544" y="402" font-size="11">RL BRANDT</text>
      <text class="brand-name" x="544" y="409" font-size="4.2">HARVEST MINISTRIES</text>
    </g>
    <text class="contact-strong" x="585" y="515">DISC</text>
  </g>

  <!-- Letterhead -->
  <g class="letterhead">
    <rect class="card-white" x="792" y="43" width="360" height="545"/>
    <g class="brand-lockup">
      <circle class="brand-mark" cx="826" cy="82" r="7"/>
      <text class="brand-name" x="837" y="88" font-size="16">RL BRANDT</text>
      <text class="brand-name" x="837" y="97" font-size="6">HARVEST MINISTRIES</text>
    </g>
    <g class="brand-lockup faint">
      <circle class="brand-mark" cx="868" cy="300" r="22"/>
      <text class="brand-name" x="900" y="316" font-size="46">RL BRANDT</text>
      <text class="brand-name" x="902" y="338" font-size="17">HARVEST MINISTRIES</text>
    </g>
    <text class="contact" x="1010" y="540">418 W. Corvell Blvd</text>
    <text class="contact" x="1010" y="547">Longview, TX 75612</text>
    <text class="contact" x="1010" y="554">rlbrandt.com</text>
    <text class="contact" x="1080" y="540">(903) 555-0148</text>
    <text class="contact" x="1080" y="547">(903) 555-0172</text>
    <text class="contact" x="1080" y="554">rlbtx7@mailvane.net</text>
    <path fill="url(#band)" d="M792 575 C950 568 1060 560 1152 548 V588 H792 Z"/>
  </g>

  <!-- Presentation caption -->
  <g class="presentation-lockup">
    <circle class="brand-mark" cx="46" cy="585" r="10"/>
    <text class="brand-name" x="62" y="592" font-size="24">RL BRANDT</text>
    <text class="brand-name" x="62" y="607" font-size="9">HARVEST MINISTRIES</text>
    <text class="caption" x="240" y="596">STATIONARY DESIGN</text>
  </g>
</svg>
</body>
</html>
```